Kick-ass motivational company vision poster

We need a company poster that communicates our vision, and keeps us motivated when the going gets tough !

We want a cool graphic design that will stand the test of time, isn't cliched, and is something we're proud to hang around the office.

TEXT
No.1 provider of high quality software development resources in London.

We combine the best of local resourcing with access to a global network, that means we always deliver.

We want our staff to work in jobs they love, and in doing so, deliver fantastic customer service.

SIZE
A1 / A2 portrait

Target Market(s)

employees

Industry/Entity Type

Professional Service

Font styles to use
Sans Serif

Requirements
Must have
• a nice graphic design - appreciate that's pretty broad but we just want a cool design - doesn't necessarily have to match our corporate look and feel (www.qovanltd.com)
Should not have
• Cliche'd use of people / photos / fist punches / clip-art etc. (you get the idea)

```html
<!DOCTYPE html>
<html lang="en">
<head>
<meta charset="utf-8">
<title>Qovan — Company Vision Poster</title>
<link rel="stylesheet" href="https://fonts.googleapis.com/css2?family=Alfa+Slab+One&family=Montserrat:wght@600;700&family=Quicksand:wght@300;400&display=swap">
<style>
  :root {
    --navy: #24418f;
    --orange: #f5892a;
    --crimson: #c01f32;
    --ink: #111111;
    --paper: #ffffff;
  }
  html, body {
    margin: 0;
    padding: 0;
    width: 849px;
    height: 1200px;
    overflow: hidden;
    background: var(--paper);
  }
  .poster {
    display: block;
    width: 849px;
    height: 1200px;
  }
  .geo-bold { font-family: "Montserrat", sans-serif; font-weight: 700; }
  .geo-light { font-family: "Quicksand", sans-serif; font-weight: 300; }
  .slab { font-family: "Alfa Slab One", serif; }
  .fill-orange { fill: var(--orange); }
  .fill-crimson { fill: var(--crimson); }
  .fill-ink { fill: var(--ink); }
  .fill-paper { fill: var(--paper); }
  .fill-navy { fill: var(--navy); }
  .frame-line { stroke: var(--navy); stroke-width: 2; fill: none; }
  .rule-thin { stroke: var(--ink); stroke-width: 2; }
</style>
</head>
<body>
<svg class="poster" viewBox="0 0 849 1200" xmlns="http://www.w3.org/2000/svg">

  <!-- Outer frame -->
  <g class="frame">
    <path class="frame-line" d="M300 1137 H40 V75 H806 V1137 H550"/>
    <circle class="fill-navy" cx="292" cy="1137" r="8"/>
    <circle class="fill-navy" cx="557" cy="1137" r="8"/>
  </g>

  <!-- Headline ribbon -->
  <g class="ribbon">
    <polygon class="fill-navy" points="122,47 742,47 718,76 742,105 122,105 146,76"/>
    <text class="geo-light fill-paper" x="432" y="93" font-size="46" font-weight="400" text-anchor="middle" textLength="510" lengthAdjust="spacingAndGlyphs">NO.1 PROVIDER OF</text>
  </g>

  <!-- Statement one -->
  <g class="statement-quality">
    <text class="geo-bold fill-orange" x="101" y="190" font-size="90" textLength="640" lengthAdjust="spacingAndGlyphs">HIGH QUALITY</text>
    <text class="geo-bold fill-ink" x="101" y="238" font-size="36" textLength="641" lengthAdjust="spacingAndGlyphs">software development resources</text>
    <rect class="fill-ink" x="101" y="252" width="110" height="96"/>
    <text class="geo-light fill-paper" font-size="46" font-weight="400" transform="translate(140 300) rotate(90)" text-anchor="middle">in</text>
    <text class="slab fill-crimson" x="222" y="347" font-size="128" textLength="520" lengthAdjust="spacingAndGlyphs">LONDON</text>
  </g>

  <rect class="fill-ink" x="102" y="372" width="640" height="10"/>

  <!-- Statement two -->
  <g class="statement-delivery">
    <line class="rule-thin" x1="106" y1="416" x2="290" y2="416"/>
    <circle class="fill-ink" cx="106" cy="416" r="4"/>
    <circle class="fill-ink" cx="290" cy="416" r="4"/>
    <text class="geo-bold fill-ink" x="427" y="430" font-size="34" text-anchor="middle">We combine</text>
    <line class="rule-thin" x1="555" y1="416" x2="738" y2="416"/>
    <circle class="fill-ink" cx="555" cy="416" r="4"/>
    <circle class="fill-ink" cx="738" cy="416" r="4"/>

    <text class="geo-bold fill-orange" x="102" y="527" font-size="90" textLength="425" lengthAdjust="spacingAndGlyphs">THE BEST</text>
    <text class="geo-bold fill-ink" x="543" y="487" font-size="34" textLength="199" lengthAdjust="spacingAndGlyphs">OF LOCAL</text>
    <text class="geo-bold fill-ink" x="543" y="524" font-size="36" textLength="199" lengthAdjust="spacingAndGlyphs">resourcing</text>

    <text class="geo-light fill-ink" x="102" y="570" font-size="40" font-weight="400" textLength="640" lengthAdjust="spacingAndGlyphs">with access to a global network,</text>
    <text class="geo-light fill-ink" x="102" y="665" font-size="82" textLength="640" lengthAdjust="spacingAndGlyphs">THAT MEANS WE</text>
    <text class="slab fill-crimson" x="102" y="737" font-size="66" textLength="640" lengthAdjust="spacingAndGlyphs">ALWAYS DELIVER</text>
  </g>

  <rect class="fill-ink" x="102" y="768" width="640" height="10"/>

  <!-- Statement three -->
  <g class="statement-people">
    <line class="rule-thin" x1="106" y1="820" x2="293" y2="820"/>
    <circle class="fill-ink" cx="106" cy="820" r="4"/>
    <circle class="fill-ink" cx="293" cy="820" r="4"/>
    <text class="geo-bold fill-ink" x="427" y="834" font-size="36" text-anchor="middle">We want</text>
    <line class="rule-thin" x1="548" y1="820" x2="738" y2="820"/>
    <circle class="fill-ink" cx="548" cy="820" r="4"/>
    <circle class="fill-ink" cx="738" cy="820" r="4"/>

    <text class="geo-light fill-ink" x="102" y="893" font-size="40" font-weight="400" textLength="337" lengthAdjust="spacingAndGlyphs">our staff to work</text>
    <text class="geo-bold fill-ink" x="102" y="943" font-size="38" textLength="337" lengthAdjust="spacingAndGlyphs">IN JOBS THEY</text>
    <text class="slab fill-crimson" x="450" y="944" font-size="112" textLength="292" lengthAdjust="spacingAndGlyphs">LOVE</text>

    <rect class="fill-navy" x="102" y="960" width="640" height="40"/>
    <text class="geo-light fill-paper" x="422" y="990" font-size="25" font-weight="400" text-anchor="middle">AND IN DOING SO,</text>
    <text class="geo-bold fill-orange" x="102" y="1036" font-size="27" textLength="640" lengthAdjust="spacingAndGlyphs">DELIVER FANTASTIC CUSTOMER SERVICE.</text>
  </g>

  <!-- Company name -->
  <text class="geo-bold fill-navy brand-name" x="425" y="1152" font-size="50" text-anchor="middle">qovan</text>
</svg>
</body>
</html>
```